Thriving Mexican import business needs a new business card

Need a refresher of our current business card. Looking for a lighter background with the logo on one side. We will want this file to be adjustable so we can change names, emails and mobile numbers.
We are open to ideas but maintaining a professional image is critical.
Thankyou,

Target Market(s)

Anyone in food industry

Industry/Entity Type

Wholesale

Contact Information for Business Card

Mark Vellanoweth
Director
Corvan Products & Liquor Pty Ltd
5B Larkfield Ct, Brimsworth VIC 3051
0491325067 (03) 95147286
mark@corvanimports.com.au
corvanimportedgoodsandspirits.com.au

Font styles to use
Serif
Other font styles liked:
• NeoGram Heavy

Requirements
Must have
• Professional yet memorable
Corvan logo
Nice to have
• Chilli or tequila/mexican food pictures
Should not have
• Dark background

```html
<!DOCTYPE html>
<html lang="en">
<head>
<meta charset="utf-8">
<title>Corvan Business Card</title>
<link href="https://fonts.googleapis.com/css2?family=Bebas+Neue&display=swap" rel="stylesheet">
<style>
  :root {
    --backdrop: #e4e2df;
    --card: #f4f4f4;
    --ink: #1c1c1c;
    --ink-soft: #2a2a2a;
    --photo-tone: #eadcd2;
    --shadow: rgba(0, 0, 0, 0.28);
  }
  * { box-sizing: border-box; margin: 0; padding: 0; }
  html, body {
    width: 1200px;
    height: 960px;
    overflow: hidden;
    background: var(--backdrop);
    font-family: "Bebas Neue", "Arial Narrow", sans-serif;
    color: var(--ink);
  }
  .canvas { position: relative; width: 1200px; height: 960px; }

  .card {
    position: absolute;
    left: 336px;
    width: 530px;
    height: 322px;
    background: var(--card);
    box-shadow: 0 3px 8px var(--shadow);
  }
  .card--front { top: 141px; }
  .card--back { top: 496px; }

  /* Front */
  .brand-square {
    position: absolute;
    left: 251px;
    top: 90px;
    width: 28px;
    height: 28px;
    background: var(--ink);
  }
  .brand-name {
    position: absolute;
    left: 0;
    width: 100%;
    top: 150px;
    text-align: center;
    font-size: 68px;
    font-weight: 400;
    line-height: 1;
    letter-spacing: 1px;
    color: var(--ink);
  }
  .brand-tagline {
    position: absolute;
    left: 0;
    width: 100%;
    top: 218px;
    text-align: center;
    font-size: 16.5px;
    letter-spacing: 0.4px;
    color: var(--ink);
  }
  .chilli-photo {
    position: absolute;
    left: 146px;
    top: 254px;
    width: 238px;
    height: 40px;
    background: var(--photo-tone);
  }

  /* Back */
  .back-brand {
    position: absolute;
    left: 0;
    width: 100%;
    top: 50px;
    text-align: center;
    font-size: 44px;
    line-height: 1;
    letter-spacing: 1px;
    color: var(--ink);
  }
  .contact-person {
    position: absolute;
    right: 282px;
    top: 189px;
    text-align: right;
    color: var(--ink-soft);
  }
  .person-name { font-size: 19px; line-height: 22px; color: var(--ink); }
  .person-role { font-size: 12px; line-height: 16px; }
  .company { margin-top: 14px; font-size: 12.5px; line-height: 18px; }

  .divider {
    position: absolute;
    left: 265px;
    top: 193px;
    width: 2px;
    height: 86px;
    background: var(--ink);
  }
  .contact-details {
    position: absolute;
    left: 282px;
    top: 194px;
    list-style: none;
    font-size: 12.5px;
    color: var(--ink-soft);
  }
  .contact-details li {
    display: flex;
    align-items: center;
    gap: 4px;
    height: 18px;
  }
  .contact-details li.gap-before { margin-top: 14px; }
  .contact-details svg { width: 11px; height: 11px; flex: none; }
</style>
</head>
<body>
<div class="canvas">

  <section class="card card--front">
    <div class="brand-square"></div>
    <h1 class="brand-name">CORVAN</h1>
    <p class="brand-tagline">MEXICAN PRODUCTS &amp;LIQUOR</p>
    <div class="chilli-photo" role="img" aria-label="Photo of a sliced chilli pepper in red, yellow and green pieces"></div>
  </section>

  <section class="card card--back">
    <div class="back-brand">CORVAN</div>

    <div class="contact-person">
      <p class="person-name">MARK VELLANOWETH</p>
      <p class="person-role">DIRECTOR</p>
      <p class="company">CORVAN PRODUCTS &amp; LIQUOR PTY LTD<br>5B LARKFIELD CT, BRIMSWORTH VIC 3051</p>
    </div>

    <div class="divider"></div>

    <ul class="contact-details">
      <li>
        <svg viewBox="0 0 24 24" aria-hidden="true"><path fill="currentColor" d="M6.6 10.8a15.1 15.1 0 0 0 6.6 6.6l2.2-2.2c.3-.3.7-.4 1-.2 1.1.4 2.3.6 3.6.6.6 0 1 .4 1 1V20c0 .6-.4 1-1 1A17 17 0 0 1 3 4c0-.6.4-1 1-1h3.5c.6 0 1 .4 1 1 0 1.3.2 2.5.6 3.6.1.3 0 .7-.2 1z"/></svg>
        0491325067
      </li>
      <li>
        <svg viewBox="0 0 24 24" aria-hidden="true"><rect x="6" y="2" width="12" height="20" rx="2" fill="none" stroke="currentColor" stroke-width="2.4"/><circle cx="12" cy="18" r="1.3" fill="currentColor"/></svg>
        (03) 95147286
      </li>
      <li class="gap-before">
        <svg viewBox="0 0 24 24" aria-hidden="true"><rect x="2" y="5" width="20" height="14" fill="none" stroke="currentColor" stroke-width="2.4"/><path d="M2 5l10 8 10-8" fill="none" stroke="currentColor" stroke-width="2.4"/></svg>
        MARK@CORVANIMPORTS.COM.AU
      </li>
      <li>
        <svg viewBox="0 0 24 24" aria-hidden="true"><g fill="none" stroke="currentColor" stroke-width="2"><circle cx="12" cy="12" r="10"/><ellipse cx="12" cy="12" rx="4.5" ry="10"/><path d="M2 12h20"/></g></svg>
        CORVANIMPORTEDGOODSANDSPIRITS.COM.AU
      </li>
    </ul>
  </section>

</div>
</body>
</html>
```